Business Card Design Project

Looking to update our business cards. We have a logo with our slogan. We are an IT firm so we wouldlike a modern look.

Industry/Entity Type

Business

```html
<!DOCTYPE html>
<html lang="en">
<head>
<meta charset="utf-8">
<title>Kestrel Inc — Business Cards</title>
<link href="https://fonts.googleapis.com/css2?family=Open+Sans:wght@400;600;700&display=swap" rel="stylesheet">
<style>
  :root {
    --backdrop: #d9d9d9;
    --card-light: #fbfbfb;
    --card-shade: #e6e6e6;
    --brand-green: #6e8a3a;
    --brand-deep: #587a22;
    --accent-lime: #a9c63c;
    --ink: #3a3a3a;
  }
  * { box-sizing: border-box; margin: 0; padding: 0; }
  html, body {
    width: 1200px; height: 900px; overflow: hidden;
    background: var(--backdrop);
    font-family: "Open Sans", Arial, sans-serif;
  }
  .card {
    position: absolute;
    left: 250px;
    width: 700px; height: 400px;
    background: linear-gradient(160deg, var(--card-light) 0%, #f1f1f1 55%, var(--card-shade) 100%);
    box-shadow: 0 6px 18px rgba(0,0,0,.25);
    overflow: hidden;
  }
  .card--front { top: 40px; }
  .card--back { top: 470px; }

  .brand {
    position: absolute;
    display: flex; align-items: center; gap: 12px;
    color: var(--brand-green);
  }
  .brand__mark {
    width: 22px; height: 22px; border-radius: 50%;
    background: var(--brand-green);
  }
  .brand__name { font-weight: 700; letter-spacing: 6px; line-height: 1; }
  .tagline {
    position: absolute;
    font-weight: 600; color: var(--ink); letter-spacing: 3px;
    text-transform: uppercase;
  }

  .card--front .brand { left: 40px; top: 40px; }
  .card--front .brand__name { font-size: 46px; }
  .card--front .tagline { left: 42px; top: 100px; font-size: 15px; }

  .person { position: absolute; right: 40px; top: 120px; text-align: right; }
  .person__name { font-size: 28px; font-weight: 600; color: var(--brand-green); letter-spacing: .5px; }
  .person__role { font-size: 15px; color: var(--ink); }

  .address {
    position: absolute; right: 40px; top: 196px; text-align: right;
    font-size: 15px; font-style: normal; color: var(--ink);
  }
  .address__company { font-size: 22px; font-weight: 700; color: var(--ink); margin-top: 4px; }

  .contact { position: absolute; font-size: 15px; color: var(--ink); line-height: 1.55; }
  .contact dt { display: inline; color: var(--accent-lime); }
  .contact dd { display: inline; }
  .contact--web { left: 40px; top: 236px; }
  .contact--phone { right: 40px; top: 280px; text-align: right; }

  .band { position: absolute; left: 0; right: 0; bottom: 0; }
  .band::before {
    content: ""; position: absolute; left: 0; right: 0; top: 0; height: 5px;
    background: var(--accent-lime);
  }
  .card--front .band { height: 36px; background: var(--brand-green); }
  .card--back .band {
    height: 110px; background: var(--brand-deep);
    display: flex; align-items: center; justify-content: center;
  }
  .band__web {
    color: #e6ecd6; font-size: 22px; font-weight: 600; letter-spacing: 9px;
    text-transform: uppercase; padding-top: 5px;
  }

  .card--back .brand { left: 0; right: 0; top: 90px; justify-content: center; }
  .card--back .brand__name { font-size: 66px; }
  .card--back .brand__mark { width: 30px; height: 30px; }
  .card--back .tagline { left: 0; right: 0; top: 176px; text-align: center; font-size: 19px; }
</style>
</head>
<body>
  <section class="card card--front" aria-label="Business card front">
    <div class="brand">
      <span class="brand__mark"></span>
      <span class="brand__name">KESTREL</span>
    </div>
    <p class="tagline">Making Technology Easy</p>

    <div class="person">
      <p class="person__name">DANIEL MARSH</p>
      <p class="person__role">Service Manager</p>
    </div>

    <address class="address">
      <p>2410 W. Harlow Ave Suite 310 Chicago IL 60612-1180</p>
      <p class="address__company">KESTREL INC</p>
    </address>

    <dl class="contact contact--web">
      <div><dt>Email:</dt> <dd>info@KestrelInc.com</dd></div>
      <div><dt>Web:</dt> <dd>www.KestrelInc.com</dd></div>
    </dl>

    <dl class="contact contact--phone">
      <div><dt>Phone:</dt> <dd>855 - 555 - 0142</dd></div>
      <div><dt>Fax:</dt> <dd>855 - 555 - 0143</dd></div>
    </dl>

    <div class="band"></div>
  </section>

  <section class="card card--back" aria-label="Business card back">
    <div class="brand">
      <span class="brand__mark"></span>
      <span class="brand__name">KESTREL</span>
    </div>
    <p class="tagline">Making Technology Easy</p>
    <div class="band"><span class="band__web">www.kestrelinc.com</span></div>
  </section>
</body>
</html>
```